***PLASTIC*** Business Card Design

1 sided business card design
The card will be screen printed on plastic, so colour and fonts must be strong.

Must use the colours in the logo eps attached (Black/Ivory/White). Other colour(s) can be added.

Four (4) examples of how the logo can be printed are included in the logo eps attached.

The business card should highlight the logo. The card will be given to architects, interior designers and builders. It should look sophisticated but also innovative.

Do not cover the whole card with colour as it is important than some of the frosted plastic card is visible.

Be creative.

Target Market(s)

architects, interior designers and builders and wealthy home owners

Industry/Entity Type

Plastic

Requirements
Must have
• Must use the colours in the logo eps attached (Black/Ivory/White). Other colour(s) can be added if necessary.

The font is Square721 ExBT but has been a little thickened. It is not essential that you use this font. The name should be a stronger version of the font than other details.

The card will be printed on PVC - see http://www.vobrelt.com.au/pricelistbcardsplastic.php

Final artwork must be print ready. You must use the printing spec at http://www.vobrelt.com.au/2011%20PVC-TW.pdf

The actual details to be typeset ono the card are:

Rory Pellam

Mobile: 0412 836157
email: info@lumaplastering.com.au
www.lumaplastering.com.au

PO Box 52, Brenton, Vic 3094

Plastering | Rendering | Cornicing

```html
<!DOCTYPE html>
<html lang="en">
<head>
<meta charset="utf-8">
<title>Luma Plastering – Business Card</title>
<link rel="stylesheet" href="https://fonts.googleapis.com/css2?family=PT+Sans:wght@400;700&display=swap">
<style>
  :root {
    --backdrop: #d9d9d9;
    --frosted: #f1f1f1;
    --frosted-edge: #e2e2e2;
    --ivory: #f8f1dc;
    --black: #0d0a0a;
    --white: #ffffff;
    --panel: #f6f9fc;
    --ink: #111111;
  }
  * { box-sizing: border-box; margin: 0; padding: 0; }
  html, body {
    width: 1200px;
    height: 900px;
    overflow: hidden;
    background: var(--backdrop);
    font-family: "PT Sans", Arial, sans-serif;
  }
  .card {
    position: absolute;
    left: 194px;
    top: 136px;
    width: 826px;
    height: 512px;
    background: var(--frosted);
    border: 1px solid var(--frosted-edge);
    border-radius: 6px;
  }
  .ivory-frame {
    position: absolute;
    left: 50px;
    top: 54px;
    width: 732px;
    height: 440px;
    background: var(--ivory);
  }
  .logo-band {
    position: absolute;
    left: 82px;
    top: 78px;
    width: 664px;
    height: 160px;
    background: var(--black);
    display: flex;
    flex-direction: column;
    align-items: center;
    justify-content: center;
    color: var(--white);
    font-weight: 700;
    text-transform: uppercase;
  }
  .logo-name {
    font-size: 84px;
    line-height: 1;
    letter-spacing: 22px;
    margin-right: -22px;
  }
  .logo-trade {
    font-size: 42px;
    line-height: 1;
    letter-spacing: 10px;
    margin-right: -10px;
    margin-top: 4px;
  }
  .contact-panel {
    position: absolute;
    left: 82px;
    top: 238px;
    width: 664px;
    height: 222px;
    background: var(--panel);
    display: flex;
    flex-direction: column;
    align-items: center;
    padding-top: 6px;
    color: var(--ink);
    font-size: 25px;
    line-height: 39px;
  }
  .services {
    position: absolute;
    left: 0;
    top: 460px;
    width: 826px;
    height: 34px;
    display: flex;
    justify-content: center;
    align-items: center;
    gap: 10px;
    color: var(--ink);
    font-size: 24px;
    letter-spacing: 0.3px;
  }
  .services .divider {
    width: 2px;
    height: 28px;
    background: var(--ink);
  }
</style>
</head>
<body>
  <div class="card">
    <div class="ivory-frame"></div>
    <div class="logo-band">
      <span class="logo-name">Luma</span>
      <span class="logo-trade">Plastering</span>
    </div>
    <div class="contact-panel">
      <p class="contact-name">Rory Pellam</p>
      <p class="contact-phone">0412 836157</p>
      <p class="contact-email">info@lumaplastering.com.au</p>
      <p class="contact-web">www.lumaplastering.com.au</p>
      <p class="contact-address">PO Box 52, Brenton, Vic 3094</p>
    </div>
    <div class="services">
      <span>PLASTERING</span>
      <span class="divider"></span>
      <span>RENDERING</span>
      <span class="divider"></span>
      <span>CORNICING</span>
    </div>
  </div>
</body>
</html>
```